Company WebSite Design
BrovaneLabs - Web Site
Creative Brief
Pharmacy/Pharmaceuticals
Brovane Labs markets a line of over-the-counter health aids
Company will use the website primary to support initial inquiries about its mission, product line and financial strength. It isn't required to be an interactive site.
Brovane used MarkSmith as its designer of its logo. You may reference the logo on this past project.
The company is providing an initial mock-up in ppt format together with mutiple formatted versions of its company logo. Please do not stray far from either. Likes: Soft corners on rectangular shapes, Calibri as font, textured background, softly textured, not heavy. Background should be used (both color and texture) for side panels when website page doesn't cover entire screen. Dislikes: Busyness or clutter on page. Prefers simple intuitive navigation
Corporate
gold, light gold, somewhat tarnished (see company logo)
dark red, almost maroon (see company logo)
light brown and or black
left side
Currently, I can not see where I can upload the draft website layout nor our company logo. If it is not available within the posted project, please request them and they will be provided to you via another avenue. Thank you for your interest.

```html
<!DOCTYPE html>
<html lang="en">
<head>
<meta charset="utf-8">
<title>BrovaneLabs</title>
<link rel="stylesheet" href="https://fonts.googleapis.com/css2?family=Questrial&family=Carlito:wght@400;700&display=swap">
<style>
:root{
  --maroon-deep:#1e0604;
  --maroon:#3a0e08;
  --brown:#5a2c14;
  --tan:#8a6a48;
  --tan-light:#a88a66;
  --panel:#0b0706;
  --panel-edge:#2a1a12;
  --gold:#d8a047;
  --gold-light:#e9c27a;
  --orange:#e07a1c;
  --text:#d8d2c8;
  --muted:#9a9088;
  --box-top:#5b5550;
  --box-bottom:#1c1917;
}
*{margin:0;padding:0;box-sizing:border-box}
html,body{width:1200px;height:581px;overflow:hidden}
body{
  position:relative;
  font-family:"Carlito",Calibri,sans-serif;
  color:var(--text);
  background:linear-gradient(180deg,var(--maroon-deep) 0,var(--maroon) 80px,var(--brown) 230px,var(--tan) 330px,var(--tan-light) 581px);
}
.site-header{position:absolute;left:0;top:0;width:1200px;height:82px;
  background:linear-gradient(180deg,#140403,#2c0906 60%,#3b0f09);border-bottom:1px solid #4a1a10}
.top-links{position:absolute;right:150px;top:6px;display:flex;gap:8px}
.top-links span{width:11px;height:11px;background:#6a3a2a;border-radius:2px}
.brand{position:absolute;left:206px;top:26px;display:flex;align-items:center;gap:8px}
.brand-dot{width:30px;height:30px;border-radius:50%;background:var(--gold)}
.brand-name{font-family:"Questrial",sans-serif;font-size:30px;color:var(--gold);letter-spacing:.5px}
.main-nav{position:absolute;left:600px;top:44px;display:flex;gap:2px}
.main-nav a{font-family:"Questrial",sans-serif;font-size:10px;color:#e8dcd0;text-decoration:none;padding:4px 8px;border-radius:3px}
.main-nav a.current{background:#4a1a10;color:#fff}
.content-panel{position:absolute;left:204px;top:118px;width:852px;height:428px;background:var(--panel);
  border:1px solid var(--panel-edge);border-radius:8px;box-shadow:0 0 18px rgba(0,0,0,.6)}
h2{font-family:"Questrial",sans-serif;font-weight:400;font-size:23px;color:#fff}
.services h2{position:absolute;left:28px;top:38px}
.featured h2{position:absolute;left:400px;top:38px}
.services-box{position:absolute;left:24px;top:86px;width:348px;height:262px;border-radius:6px;
  background:linear-gradient(180deg,var(--box-top),var(--box-bottom));padding:12px 14px}
.services-box p{font-size:8.5px;line-height:11px;color:#c8c2bc;text-transform:uppercase}
.service-list{list-style:none;margin-top:26px}
.service-list li{font-size:8.5px;line-height:17.5px;color:#efe8e0;text-transform:uppercase;padding-left:14px;position:relative}
.service-list li::before{content:"";position:absolute;left:0;top:6px;border-left:5px solid var(--orange);border-top:3px solid transparent;border-bottom:3px solid transparent}
.featured-intro{position:absolute;left:400px;top:88px;width:380px}
.featured-intro .lead{font-size:8.5px;color:var(--orange);text-transform:uppercase}
.featured-intro p{font-size:8.5px;line-height:11px;color:#c8c2bc;text-transform:uppercase;margin-top:10px}
.feature{position:absolute;left:400px;width:380px;display:flex;gap:12px}
.feature .photo{flex:none;width:115px;border-radius:3px}
.feature .copy{font-size:8px;line-height:10.5px;text-transform:uppercase;color:#c8c2bc}
.feature .copy b{display:block;color:var(--orange);font-weight:400}
.photo-one{height:58px;background:linear-gradient(135deg,#d8d8d8,#6a6a6a)}
.photo-two{height:72px;background:linear-gradient(135deg,#c8b8a8,#3a3a44)}
.photo-three{height:50px;background:linear-gradient(135deg,#b89878,#3a2a20)}
.scrollbar{position:absolute;left:786px;top:88px;width:5px;height:258px;background:#2a2420;border-radius:3px}
.scrollbar span{display:block;height:40px;background:var(--orange);border-radius:3px}
.divider{position:absolute;left:24px;right:24px;top:358px;border-top:1px solid #2a221e}
.welcome h2{position:absolute;left:28px;top:366px}
.welcome p{position:absolute;left:28px;top:398px;width:560px;font-size:8.5px;line-height:11px;color:var(--orange);text-transform:uppercase}
.share{position:absolute;left:756px;top:373px;display:flex;gap:5px}
.share span{width:14px;height:14px;border-radius:3px;background:#7a8a9a}
.share span:first-child{background:var(--orange)}
.site-footer{position:absolute;left:204px;top:556px;width:852px;height:20px;display:flex;justify-content:space-between;
  align-items:center;padding:0 10px;font-size:8.5px;color:var(--gold-light);text-transform:uppercase;
  background:linear-gradient(180deg,#3a2416,#24150c);border-radius:4px}
</style>
</head>
<body>
<header class="site-header">
  <div class="top-links"><span></span><span></span><span></span></div>
  <div class="brand"><span class="brand-dot"></span><span class="brand-name">BrovaneLabs</span></div>
  <nav class="main-nav">
    <a class="current" href="#">HOME</a><a href="#">ABOUT</a><a href="#">PRODUCTS</a><a href="#">SERVICES</a><a href="#">SUPPORT</a><a href="#">CLIENTS</a><a href="#">NEWS</a><a href="#">CONTACTS</a>
  </nav>
</header>

<main class="content-panel">
  <section class="services">
    <h2>Services List</h2>
    <div class="services-box">
      <p>Praesent vestibulum molestie lacus aenean nonummy hendrerit mauris phasellus porta fusce suscipit varius mi cum sociis natoque penatibus et magnis dis parturient montes nascetur ridiculus mus nulla dui fusce feugiat malesuada odio morbi nunc odio gravida at cursus nec luctus a lorem.</p>
      <ul class="service-list">
        <li>Sed ut perspiciatis unde omnis iste natus error sit</li>
        <li>Voluptatem accusantium doloremque laudantium</li>
        <li>Totam rem aperiam, eaque ipsa quae ab illo inventore</li>
        <li>Veritatis et quasi architecto beatae vitae dicta sunt</li>
        <li>Explicabo nemo enim ipsam voluptatem quia voluptas</li>
        <li>Sit aspernatur aut odit aut fugit, sed quia consequuntur</li>
        <li>Magni dolores eos qui ratione voluptatem sequi</li>
        <li>Nesciunt neque porro quisquam est, qui dolorem ipsum</li>
        <li>Quia dolor sit amet, consectetur, adipisci velit, sed</li>
      </ul>
    </div>
  </section>

  <section class="featured">
    <h2>Featured Services</h2>
    <div class="featured-intro">
      <div class="lead">Lorem ipsum dolor sit amet, consectetuer adipiscing elit</div>
      <p>Vestibulum iaculis lacinia est. Proin dictum elementum velit. Fusce euismod consequat ante. Lorem ipsum dolor sit amet, consectetuer adipiscing elit. Pellentesque sed dolor. Aliquam congue fermentum nisl. Mauris accumsan nulla vel diam sed in lacus ut enim adipiscing.</p>
    </div>
    <div class="feature" style="top:156px">
      <div class="photo photo-one" role="img" aria-label="Photo of hands holding health aid products"></div>
      <div class="copy"><b>Proin dictum elementum velit fusce euismod consequat ante</b>Lorem ipsum dolor sit amet, consectetuer adipiscing elit pellentesque sed dolor aliquam congue fermentum.</div>
    </div>
    <div class="feature" style="top:222px">
      <div class="photo photo-two" role="img" aria-label="Photo of a business team"></div>
      <div class="copy"><b>Vestibulum iaculis lacinia est</b>Proin dictum elementum velit fusce euismod consequat ante lorem ipsum dolor sit amet, consectetuer adipiscing elit mauris accumsan nulla.</div>
    </div>
    <div class="feature" style="top:302px">
      <div class="photo photo-three" role="img" aria-label="Photo of pharmacy products"></div>
      <div class="copy"><b>Pellentesque sed dolor aliquam</b>Congue fermentum nisl mauris accumsan nulla vel diam sed in lacus ut enim adipiscing aliquet.</div>
    </div>
    <div class="scrollbar"><span></span></div>
  </section>

  <div class="divider"></div>

  <section class="welcome">
    <h2>Welcome</h2>
    <p>Lorem ipsum dolor sit amet, consectetuer adipiscing elit. Sed diam nonummy nibh euismod tincidunt ut laoreet dolore magna aliquam erat volutpat ut wisi enim ad minim veniam quis nostrud exerci tation.</p>
    <div class="share"><span></span><span></span><span></span><span></span><span></span><span></span></div>
  </section>
</main>

<footer class="site-footer">
  <span>Copyright &nbsp;|&nbsp; Privacy Policy</span>
  <span>Back to top</span>
</footer>
</body>
</html>
```